Orchard sparkle graphic

We need a graphic for an offer in our dental office for Orchard sparkle treatment. Once enrolled the patient will be given a whitening treatment once a year for as long as they are a patient with our office. This means that they must come in for their routine cleanings. Fine print: There is an enrollment fee of 99 dollars and contact us for additional rules and conditions. We need a logo or picture that we can use on our home page slide show that is clean and makes you think of healthy white teeth. Our logo to our practice has been enclosed as well to give you style direction. We don't want this logo to have a ton of wording on it, it needs to be clean and modern looking. The name of the program is call Orchard Sparkle and we need to have the fine print on the ad as well, but we will be looking for entries that incorporate our logo that is submitted and can make this offer really stand out.

Dental

```html
<!DOCTYPE html>
<html lang="en">
<head>
<meta charset="utf-8">
<title>Orchard Sparkle Offer Banners</title>
<link rel="stylesheet" href="https://fonts.googleapis.com/css2?family=Chewy&family=Courier+Prime&family=Nunito:wght@500&family=Roboto+Condensed:wght@400;700&family=Roboto:wght@100;300;700&display=swap">
<style>
  :root {
    --brand-blue: #0fb0ec;
    --brand-blue-light: #8fd6f4;
    --ink-dark: #1c3a40;
    --ink-grey: #8a8a8a;
    --paper: #ffffff;
    --canvas-edge: #e2e2e2;
    --skin-light: #f6e3d8;
    --skin-mid: #e8c2ae;
    --skin-deep: #d49d86;
  }
  * { box-sizing: border-box; margin: 0; padding: 0; }
  html, body { width: 1200px; height: 902px; overflow: hidden; background: var(--paper); }
  .canvas {
    position: relative; width: 1200px; height: 902px;
    border: 1px solid var(--canvas-edge); background: var(--paper); overflow: hidden;
  }
  .banner {
    position: absolute; left: 103px; width: 994px; height: 364px;
    border: 6px solid var(--brand-blue); background: var(--paper); overflow: hidden;
  }
  .banner--classic { top: 72px; }
  .banner--playful { top: 467px; }
  .banner > * { position: absolute; }

  .photo-smile {
    top: 0; right: 0; height: 100%;
    background: radial-gradient(ellipse at 62% 45%, var(--skin-mid) 0%, var(--skin-light) 45%, rgba(255,255,255,0) 80%);
  }
  .banner--classic .photo-smile { left: 451px; }
  .banner--playful .photo-smile {
    left: 591px;
    background: radial-gradient(ellipse at 55% 50%, var(--skin-deep) 0%, var(--skin-mid) 35%, var(--skin-light) 65%, rgba(255,255,255,0) 95%);
  }

  .wordmark {
    font-family: "Nunito", sans-serif; font-weight: 500; color: var(--ink-dark); white-space: nowrap;
  }
  .banner--classic .wordmark { left: 53px; top: 72px; font-size: 21px; }
  .banner--playful .wordmark { left: 15px; top: 43px; font-size: 13px; }

  .headline-thin {
    left: 51px; top: 110px;
    font-family: "Roboto", sans-serif; font-weight: 100; font-size: 64px; line-height: 61px;
    color: var(--brand-blue); letter-spacing: 1px;
  }
  .tagline {
    left: 265px; top: 265px;
    font-family: "Roboto Condensed", sans-serif; font-size: 20px; color: var(--brand-blue);
  }
  .cta-bold {
    left: 53px; top: 310px;
    font-family: "Roboto", sans-serif; font-weight: 700; font-size: 15px; color: var(--ink-dark);
  }

  .price-badge {
    border-radius: 50%; background: var(--brand-blue); color: var(--paper);
    display: flex; flex-direction: column; align-items: center; justify-content: center;
    font-family: "Roboto Condensed", sans-serif; text-align: center;
  }
  .price-badge .price-label { font-weight: 400; }
  .price-badge .price-amount { font-weight: 700; line-height: 0.9; }
  .banner--classic .price-badge { left: 406px; top: 104px; width: 150px; height: 150px; }
  .banner--classic .price-label { font-size: 19px; margin-top: -12px; }
  .banner--classic .price-amount { font-size: 66px; }
  .banner--playful .price-badge { left: 461px; top: 115px; width: 110px; height: 110px; }
  .banner--playful .price-label { font-size: 14px; margin-top: -8px; }
  .banner--playful .price-amount { font-size: 48px; }

  .headline-script {
    left: 100px; top: 110px; width: 360px; text-align: center;
    font-family: "Chewy", cursive; font-size: 52px; line-height: 52px; color: var(--brand-blue);
  }
  .headline-script .line-soft { color: var(--brand-blue-light); }
  .offer-label {
    left: 180px; top: 236px; width: 220px; text-align: center;
    font-family: "Roboto", sans-serif; font-weight: 300; font-size: 34px; color: var(--brand-blue);
  }
  .cta-contact {
    left: 88px; top: 306px;
    font-family: "Courier Prime", monospace; font-size: 15px; color: var(--ink-grey); white-space: nowrap;
  }
</style>
</head>
<body>
<main class="canvas">
  <section class="banner banner--classic">
    <div class="photo-smile" role="img" aria-label="Photograph of a smiling woman's lower face showing bright white teeth"></div>
    <div class="wordmark">harbor bay dental studio</div>
    <h1 class="headline-thin">ORCHARD<br>SPARKLE<br>OFFER.</h1>
    <p class="tagline">An offer you just cant resist</p>
    <div class="price-badge">
      <span class="price-label">JUST</span>
      <span class="price-amount">99$</span>
    </div>
    <p class="cta-bold">TAKE AN APPOINTMENT TODAY.</p>
  </section>

  <section class="banner banner--playful">
    <div class="photo-smile" role="img" aria-label="Photograph of a laughing woman's mouth with white teeth"></div>
    <div class="wordmark">harbor bay dental studio</div>
    <h2 class="headline-script">Orchard<br><span class="line-soft">Sparkle</span></h2>
    <div class="price-badge">
      <span class="price-label">JUST</span>
      <span class="price-amount">99$</span>
    </div>
    <p class="offer-label">OFFER</p>
    <p class="cta-contact">Take an appointment today. CALL US ON- +15550142288</p>
  </section>
</main>
</body>
</html>
```